Flyer for the Lumen 2025 Conference

I am looking to produce a flyer for our upcoming conference, Lumen 2025. This is an annual conference that we plan to publicize on social media. The ideal designer will create a flyer that is eye-catching and effectively communicates the key information. Please see attached our logo, speaker photo, and flyer content.

Target Market(s)

All demographics

Industry/Entity Type

Christian

Font styles to use
Sans Serif

Requirements
Should not have
• Cross, church

```html
<!DOCTYPE html>
<html lang="en">
<head>
<meta charset="utf-8">
<title>Lumen 2025 Prophetic Conference Flyer</title>
<link rel="stylesheet" href="https://fonts.googleapis.com/css2?family=Bebas+Neue&family=Montserrat:ital,wght@0,500;0,600;0,700;1,500&display=swap">
<style>
  :root {
    --blue-deep: #0b5a92;
    --blue-mid: #1a78b4;
    --blue-mist: #8cc7ea;
    --orange: #f39320;
    --white: #ffffff;
    --ink: #111111;
  }
  * { margin: 0; padding: 0; box-sizing: border-box; }
  html, body { width: 802px; height: 1200px; overflow: hidden; background: var(--blue-deep); }
  .flyer {
    position: relative; width: 802px; height: 1200px; overflow: hidden;
    background: linear-gradient(180deg, #2a8fcf 0%, var(--blue-mid) 30%, var(--blue-deep) 62%, var(--blue-deep) 100%);
    font-family: "Montserrat", sans-serif; color: var(--white);
  }
  .stage-photo {
    position: absolute; left: 0; top: 0; width: 802px; height: 690px;
    background:
      radial-gradient(ellipse 220px 160px at 200px 120px, rgba(200,230,250,.75), transparent 70%),
      radial-gradient(ellipse 220px 170px at 610px 110px, rgba(200,230,250,.75), transparent 70%),
      radial-gradient(ellipse 200px 300px at 400px 420px, rgba(20,80,150,.9), transparent 75%),
      linear-gradient(180deg, rgba(140,199,234,.4), rgba(11,90,146,0) 100%);
  }
  .headline { position: absolute; left: 0; top: 420px; width: 802px; }
  .headline svg { display: block; }
  .topic { position: absolute; left: 0; top: 752px; width: 802px; text-align: center; }
  .topic-label { font-family: "Bebas Neue", sans-serif; font-size: 40px; letter-spacing: 4px; line-height: 1; }
  .topic-line { font-size: 25px; font-weight: 700; margin-top: 6px; white-space: nowrap; }
  .topic-line .speaker-name { font-weight: 500; font-style: italic; }
  .dates { position: absolute; top: 866px; left: 0; width: 802px; }
  .date-card {
    position: absolute; width: 152px; height: 156px; background: var(--white);
    border: 5px solid var(--orange); border-radius: 28px; color: var(--ink);
    text-align: center; font-family: "Bebas Neue", sans-serif; padding-top: 14px;
  }
  .date-card .month { font-size: 32px; line-height: 1; }
  .date-card .day { font-size: 72px; line-height: .9; }
  .date-card .time { font-size: 15px; line-height: 1.05; margin-top: 4px; }
  .details { position: absolute; left: 52px; top: 1050px; width: 500px; }
  .details h3 { font-size: 19px; font-weight: 700; }
  .details .address { font-size: 14px; font-weight: 500; line-height: 1.1; margin-top: 4px; }
  .app-pill {
    display: inline-block; margin-top: 12px; background: var(--orange); color: var(--ink);
    font-size: 13px; font-weight: 600; border-radius: 12px; padding: 2px 12px; width: 438px;
  }
  .contacts { display: flex; gap: 30px; margin-top: 10px; font-size: 13.5px; font-weight: 500; white-space: nowrap; }
  .contacts span { display: inline-flex; align-items: center; gap: 6px; }
  .brand { position: absolute; left: 590px; top: 1095px; display: flex; align-items: center; gap: 10px; }
  .brand-dot { width: 16px; height: 16px; border-radius: 50%; background: var(--orange); }
  .brand-name { font-family: "Montserrat", sans-serif; font-weight: 700; font-size: 36px; color: var(--white); letter-spacing: 1px; }
</style>
</head>
<body>
<main class="flyer">
  <div class="stage-photo" role="img" aria-label="Photo of the speaker in a blue blazer standing against a smoky blue stage backdrop"></div>

  <div class="headline">
    <svg width="802" height="300" viewBox="0 0 802 300">
      <text x="401" y="50" text-anchor="middle" font-family="Bebas Neue, sans-serif" font-size="56" fill="#ffffff" textLength="270" lengthAdjust="spacingAndGlyphs">LUMEN 2025 A</text>
      <text x="401" y="228" text-anchor="middle" font-family="Bebas Neue, sans-serif" font-size="236" fill="#f39320" textLength="652" lengthAdjust="spacingAndGlyphs">PROPHETIC</text>
      <text x="401" y="298" text-anchor="middle" font-family="Bebas Neue, sans-serif" font-size="80" fill="#ffffff" textLength="438" lengthAdjust="spacingAndGlyphs">CONFERENCE</text>
    </svg>
  </div>

  <section class="topic">
    <p class="topic-label">TOPIC:</p>
    <p class="topic-line">The Voice Of The LordSpeaker: <span class="speaker-name">Prophet Elias Marrow</span></p>
  </section>

  <section class="dates">
    <div class="date-card" style="left:115px">
      <p class="month">DECEMBER</p><p class="day">26TH</p>
      <p class="time">6:30PM - 9:00PM<br>SATURDAY</p>
    </div>
    <div class="date-card" style="left:325px">
      <p class="month">DECEMBER</p><p class="day">27TH</p>
      <p class="time">5:30PM - 8:00PM<br>SUNDAY</p>
    </div>
    <div class="date-card" style="left:535px">
      <p class="month">DECEMBER</p><p class="day">29TH</p>
      <p class="time" style="margin-top:10px">4:30PM - 7:00PM</p>
    </div>
  </section>

  <section class="details">
    <h3>Location:</h3>
    <p class="address">The Harborview Arts Center 218 Linden Avenue<br>Millbrook, Maine 04010</p>
    <p class="app-pill">Download the Veraly App to stay updated on the event</p>
    <div class="contacts">
      <span><svg width="13" height="13" viewBox="0 0 24 24"><path d="M6.6 10.8a15 15 0 0 0 6.6 6.6l2.2-2.2a1 1 0 0 1 1-.25 11.4 11.4 0 0 0 3.6.6 1 1 0 0 1 1 1V20a1 1 0 0 1-1 1A17 17 0 0 1 3 4a1 1 0 0 1 1-1h3.5a1 1 0 0 1 1 1c0 1.25.2 2.45.6 3.6a1 1 0 0 1-.25 1z" fill="#fff"/></svg>207 555 0148</span>
      <span><svg width="15" height="11" viewBox="0 0 24 17"><rect x="1" y="1" width="22" height="15" fill="none" stroke="#fff" stroke-width="2"/><path d="M1 1l11 8 11-8" fill="none" stroke="#fff" stroke-width="2"/></svg>hello@veraly.org</span>
      <span><svg width="14" height="14" viewBox="0 0 24 24" fill="none" stroke="#fff" stroke-width="2"><circle cx="12" cy="12" r="10"/><ellipse cx="12" cy="12" rx="4.5" ry="10"/><path d="M2 12h20"/></svg>www.veraly.org</span>
    </div>
  </section>

  <div class="brand">
    <span class="brand-dot"></span>
    <span class="brand-name">VERALY</span>
  </div>
</main>
</body>
</html>
```